The maple crew

I want it as prefession and attractive as possible we are a lawnmowing business

Phone number 605-318-2264
Name- Carlos Whitfield
Email- themaplecrewsd@fernpost.com

```html
<!DOCTYPE html>
<html lang="en">
<head>
<meta charset="UTF-8">
<title>The Maple Crew – Business Card</title>
<link href="https://fonts.googleapis.com/css2?family=Roboto+Condensed:wght@700&family=Roboto:wght@400&display=swap" rel="stylesheet">
<style>
  :root {
    --stage: #5a5a5a;
    --paper: #ffffff;
    --forest: #0b5a34;
    --back-green: #085e3b;
    --leaf: #5bbf45;
    --mint: #2fd39a;
    --ghost: rgba(228, 236, 232, 0.75);
    --ghost-clear: rgba(228, 236, 232, 0);
    --rule: #cfd2d1;
    --ink: #555555;
  }
  * { box-sizing: border-box; margin: 0; padding: 0; }
  html, body {
    width: 1200px; height: 1200px; overflow: hidden;
    background: var(--stage);
  }
  .card {
    position: absolute;
    width: 690px; height: 394px;
    overflow: hidden;
  }
  .card-front { left: 266px; top: 158px; background: var(--paper); }
  .card-back { left: 260px; top: 651px; height: 395px; background: var(--back-green); }

  .mower-art {
    position: absolute; left: 0; top: 170px;
    width: 380px; height: 224px;
    background: radial-gradient(closest-side, var(--ghost) 0%, var(--ghost-clear) 100%);
  }
  .grass-art {
    position: absolute; left: 360px; top: 300px;
    width: 340px; height: 110px;
    background: radial-gradient(closest-side, var(--ghost) 0%, var(--ghost-clear) 100%);
  }
  .brand-name {
    position: absolute; right: 50px; top: 52px;
    font-family: "Roboto Condensed", sans-serif;
    font-weight: 700; font-size: 40px; letter-spacing: 1px;
    text-transform: uppercase; color: var(--forest);
  }
  .person-name {
    position: absolute; left: 49px; top: 238px;
    font-family: "Roboto Condensed", sans-serif;
    font-weight: 700; font-size: 29px; color: var(--forest);
    text-transform: uppercase;
  }
  .divider {
    position: absolute; left: 49px; top: 281px;
    width: 596px; height: 1px; background: var(--rule);
  }
  .contact {
    position: absolute; left: 43px;
    display: flex; align-items: center; gap: 10px;
    font-family: "Roboto", sans-serif; font-size: 16.5px; color: var(--ink);
  }
  .contact svg { width: 16px; height: 16px; flex: none; }
  .contact-phone { top: 290px; }
  .contact-email { top: 310px; }
  .band-light {
    position: absolute; left: 0; bottom: 0;
    width: 380px; height: 15px; background: var(--leaf);
  }
  .band-dark {
    position: absolute; left: 0; bottom: 0; width: 690px; height: 34px;
  }
  .website {
    position: absolute; right: 44px; bottom: 6px;
    font-family: "Roboto", sans-serif; font-size: 16px; color: #ffffff;
  }
  .back-brand {
    position: absolute; left: 0; right: 0; top: 165px;
    text-align: center;
    font-family: "Roboto Condensed", sans-serif;
    font-weight: 700; font-size: 52px; letter-spacing: 2px;
    text-transform: uppercase; color: var(--mint);
  }
</style>
</head>
<body>
  <section class="card card-front">
    <div class="mower-art" role="img" aria-label="Faint silhouette of a person pushing a lawn mower"></div>
    <div class="grass-art" role="img" aria-label="Faint grass blades decoration"></div>

    <div class="brand-name">The maple crew</div>

    <h1 class="person-name">Carlos Whitfield</h1>
    <div class="divider"></div>

    <div class="contact contact-phone">
      <svg viewBox="0 0 24 24" aria-hidden="true"><path fill="#5bbf45" d="M6.6 10.8a15.1 15.1 0 0 0 6.6 6.6l2.2-2.2c.3-.3.7-.4 1-.2 1.1.4 2.3.6 3.6.6.6 0 1 .4 1 1V20c0 .6-.4 1-1 1A17 17 0 0 1 3 4c0-.6.4-1 1-1h3.5c.6 0 1 .4 1 1 0 1.3.2 2.5.6 3.6.1.3 0 .7-.2 1z"/></svg>
      <span>605-318-2264</span>
    </div>
    <div class="contact contact-email">
      <svg viewBox="0 0 24 24" aria-hidden="true"><rect x="2" y="5" width="20" height="14" fill="#5bbf45"/><path d="M2 5l10 8 10-8" fill="none" stroke="#fff" stroke-width="1.6"/></svg>
      <span>themaplecrewsd@fernpost.com</span>
    </div>

    <div class="band-light"></div>
    <svg class="band-dark" viewBox="0 0 690 34" preserveAspectRatio="none" aria-hidden="true">
      <polygon points="364,34 366,34 396,0 690,0 690,34" fill="#0b5e36"/>
    </svg>
    <div class="website">www.themaplecrewsd.com</div>
  </section>

  <section class="card card-back">
    <div class="back-brand">The maple crew</div>
  </section>
</body>
</html>
```